The Mark Lantern Master Deck & Brand Guidelines Execution

You’ll be providing designers with your client’s brand communications guidelines (the attached file). The task is to:

Create a sharp, savvy, professional TML-branded PowerPoint template

Must adhere to TML’s brand identity (royal blue, metallic accents, minimal, modern).

Designed to be used repeatedly for clients, with flexible layouts.

Rebuild the Client’s Brand Guidelines using this new TML template

Designers take the client’s content (the provided brand comms guidelines) and recreate them inside the TML-branded template.

The final product should show:

The client’s actual guidelines (their text, logos, and assets)

Formatted beautifully in TML’s brand style (so every guidelines deck we create for clients has a consistent “The Mark Lantern” look and feel).

Deliverables

Editable PPTX master template (with multiple layouts: cover, section dividers, content, data, quotes, contact).

Editable Google Slides version.

A client-facing guidelines deck: the attached content, rebuilt in the new TML template.

Design Requirements

Must be sharp, savvy, professional.

Must strictly follow TML brand guidelines.

Must show how client content sits within TML’s branded framework (e.g. how a client’s logo, tone of voice, colour palette sits inside the TML deck design).

Think consultancy-level polish: minimal, elegant, structured.

Important Conditions

All contact must remain on the contest platform.

No direct outreach to me or my clients — violations will result in disqualification and reporting.

Primary colours - purple and black. Minimal sunflower yellow. Visit our website for more insight www.themarklantern.com.au

Minimalist styles only.

Font styles to use
Sans Serif

Requirements
Must have
• Google slides, professional
Should not have
• Stock imagery

```html
<!DOCTYPE html>
<html lang="en">
<head>
<meta charset="utf-8">
<title>The Mark Lantern – Brand &amp; Positioning Guidelines</title>
<link href="https://fonts.googleapis.com/css2?family=Manrope:wght@300;400;500;600;700;800&display=swap" rel="stylesheet">
<style>
:root{
  --canvas:#cbcbcf;
  --purple:#553a8c;
  --purple-deep:#3a2474;
  --ink:#111016;
  --white:#ffffff;
  --lavender:#bdb5d4;
  --lilac-a:#dcbdf2;
  --lilac-b:#a27fe0;
  --line:#b9b3c9;
}
*{box-sizing:border-box;margin:0;padding:0}
html,body{width:970px;height:1200px;overflow:hidden;background:var(--canvas);font-family:"Manrope",sans-serif;color:var(--ink)}
.board{position:relative;width:970px;height:1200px}
.slide{position:absolute;width:414px;height:232px;overflow:hidden;background:var(--white);box-shadow:0 2px 6px rgba(0,0,0,.12)}
.abs{position:absolute}
.wordmark{font-family:"Manrope",sans-serif;font-weight:800;letter-spacing:-.06em;color:var(--ink);white-space:nowrap;line-height:1}
.wordmark.light{color:var(--white)}
.heading{font-weight:700;color:var(--purple);text-transform:uppercase;line-height:1.1;letter-spacing:-.01em}
.photo{position:absolute}

/* cover */
.cover{left:56px;top:61px;background:linear-gradient(135deg,var(--lilac-a),var(--lilac-b))}
.cover .wordmark{left:22px;top:28px;font-size:20px}
.cover .title{left:26px;top:78px;font-size:22.5px;line-height:27px;color:var(--purple-deep);font-weight:800;text-transform:uppercase}
.cover .sub{left:28px;top:180px;font-size:10.5px;line-height:15.5px;color:var(--ink);font-weight:400}
.cover .photo{right:0;top:0;width:208px;height:232px;background:linear-gradient(180deg,#c6a9ec 0%,#b795e6 55%,#efe9f1 100%)}

/* promise */
.promise{left:499px;top:61px}
.promise .wordmark{left:17px;top:24px;font-size:15px}
.promise .heading{left:18px;top:76px;font-size:16px}
.promise .bar{left:20px;top:112px;width:1px;height:67px;background:var(--purple)}
.promise .quote{left:35px;top:112px;width:150px;font-size:9.4px;line-height:16px;color:var(--purple);font-weight:400}
.promise .photo{left:235px;top:0;width:179px;height:232px;background:linear-gradient(160deg,#eef0f2 0%,#8fb6dc 45%,#b8464f 100%)}
.badge{position:absolute;width:55px;height:55px;border-radius:50%;background:var(--purple);color:var(--white);display:flex;flex-direction:column;align-items:center;justify-content:center;gap:3px;font-size:5.2px;font-weight:700;text-transform:uppercase}

/* value props */
.values{left:56px;top:336px}
.values .panel{left:207px;top:0;width:207px;height:232px;background:var(--purple)}
.values .photo{left:221px;top:14px;width:193px;height:218px;background:linear-gradient(140deg,#f4f2f1 0%,#d9d3cf 45%,#8d7466 100%)}
.values .wordmark{left:13px;top:15px;font-size:15px}
.values .heading{left:13px;top:48px;font-size:16px;line-height:19px}
.vbox{position:absolute;width:153.5px;height:51.5px;background:var(--purple);color:var(--white);padding:8px 8px 0 16px}
.vbox h3{font-size:8.6px;font-weight:600;margin-bottom:4px}
.vbox p{font-size:5.9px;line-height:8.5px;font-weight:400;width:110px}

/* voice */
.voice{left:499px;top:336px}
.voice .wordmark{left:13px;top:17px;font-size:15px}
.voice .heading{left:14px;top:38px;font-size:15.5px}
.voice .photo{left:16px;top:66px;width:203px;height:148.5px;background:linear-gradient(135deg,#b7c8d8 0%,#e6dcd2 50%,#f3f3f3 100%)}
.tbox{position:absolute;left:239px;width:153px;height:30px;background:var(--purple);color:var(--white);padding:5px 11px}
.tbox h3{font-size:7.6px;font-weight:600;line-height:10px}
.tbox p{font-size:5.6px;line-height:8px;font-weight:400}

/* messages */
.messages{left:56px;top:606px}
.messages .wordmark{left:0;width:414px;text-align:center;top:17px;font-size:15px}
.messages .heading{left:0;width:414px;text-align:center;top:52px;font-size:16px}
.messages .band{left:0;top:90.5px;width:414px;height:122.5px;background:var(--purple);display:flex;padding:16px 0}
.msg{flex:1;display:flex;flex-direction:column;align-items:center;color:var(--white);text-align:center;border-right:1px solid rgba(255,255,255,.25)}
.msg:last-child{border-right:none}
.msg svg{width:26px;height:28px;margin:8px 0 18px}
.msg p{font-size:8.1px;line-height:12px;font-weight:300}

/* section divider */
.divider{left:499px;top:606px;background:var(--lavender);text-align:center}
.divider .wordmark{left:0;width:414px;top:25px;font-size:24px}
.divider .num{left:0;width:414px;top:72px;font-size:60px;font-weight:800;color:var(--purple-deep);letter-spacing:-.02em;line-height:1}
.divider .heading{left:0;width:414px;top:160px;font-size:21px;line-height:26px;color:var(--purple-deep)}

/* overview */
.overview{left:57px;top:877px}
.overview .head{left:0;top:0;width:414px;height:37px;background:var(--purple)}
.overview .wordmark{left:13px;top:11px;font-size:15px}
.overview .head h2{position:absolute;right:13px;top:8px;font-size:15px;font-weight:600;color:var(--white)}
.card{position:absolute;width:125.5px;height:48.6px;border:1px solid var(--line);background:var(--white);padding:8px 5px 0 28px}
.card svg{position:absolute;left:8px;top:9px;width:14px;height:14px}
.card h3{font-size:7px;font-weight:600;color:var(--purple);margin-bottom:3px}
.card p{font-size:5.1px;line-height:7.4px;color:var(--ink);font-weight:400}
.overview .photo{left:145px;top:157.6px;width:257px;height:64px;background:linear-gradient(90deg,#c9d8df 0%,#e6e2de 45%,#9fb0b6 100%)}

/* closing */
.closing{left:502px;top:875px;background:var(--purple)}
.closing .wordmark{left:0;width:414px;text-align:center;top:46px;font-size:24px}
.closing .rule{left:116px;width:182px;height:1px;background:rgba(255,255,255,.5)}
.closing .thanks{left:0;width:414px;text-align:center;top:117px;font-size:36px;font-weight:300;color:var(--white);letter-spacing:-.01em;line-height:1.2}
</style>
</head>
<body>
<main class="board">

  <!-- Cover -->
  <section class="slide cover">
    <div class="abs wordmark">The Mark Lantern</div>
    <h1 class="abs title">Marisol’s<br>Orthodontic<br>Clinics</h1>
    <p class="abs sub">Brand &amp; Positioning Guidelines<br>Phase 1 Foundation Strategy</p>
    <div class="photo" role="img" aria-label="Portrait of a smiling clinician in a white top against a lilac backdrop"></div>
  </section>

  <!-- Brand promise -->
  <section class="slide promise">
    <div class="abs wordmark">The Mark Lantern</div>
    <h2 class="abs heading">Brand Promise</h2>
    <div class="abs bar"></div>
    <p class="abs quote">"Precision orthodontics with genuine care - where 20+ years of expertise meets authentic patient relationships"</p>
    <div class="photo" role="img" aria-label="Orthodontist and smiling patient in a clinic"></div>
    <div class="badge" style="left:208.5px;top:72.5px">
      <svg width="20" height="20" viewBox="0 0 24 24" fill="none" stroke="#fff" stroke-width="1.4"><circle cx="11" cy="13" r="8"/><circle cx="11" cy="13" r="4.5"/><circle cx="11" cy="13" r="1.2"/><path d="M11 13 20 4M17 3v4h4"/></svg>
      <span>Precision</span>
    </div>
    <div class="badge" style="left:208.5px;top:142.5px">
      <svg width="20" height="20" viewBox="0 0 24 24" fill="none" stroke="#fff" stroke-width="1.4"><path d="M12 11c-3-3-6-1-5 2l5 4 5-4c1-3-2-5-5-2z"/><path d="M3 12v5l5 4h4M21 12v5l-5 4h-4"/></svg>
      <span>Genuine Care</span>
    </div>
  </section>

  <!-- Core value propositions -->
  <section class="slide values">
    <div class="abs panel"></div>
    <div class="photo" role="img" aria-label="Patient smiling in a dental chair beside instruments"></div>
    <div class="abs wordmark">The Mark Lantern</div>
    <h2 class="abs heading">Core Value<br>Propositions</h2>
    <div class="vbox" style="left:13px;top:103.5px"><h3>Clinical Excellence</h3><p>Fellowship-trained specialist handling complex cases others can’t</p></div>
    <div class="vbox" style="left:176px;top:103.5px"><h3>Authentic Relationships</h3><p>Genuine care overtransactional interactions</p></div>
    <div class="vbox" style="left:13px;top:161.5px"><h3>Holistic Approach</h3><p>Function and aesthetics for long-term health outcomes</p></div>
    <div class="vbox" style="left:176px;top:161.5px"><h3>Inclusive Expertise</h3><p>Trusted care for all ages and diverse needs</p></div>
  </section>

  <!-- Voice & tone -->
  <section class="slide voice">
    <div class="abs wordmark">The Mark Lantern</div>
    <h2 class="abs heading">Brand Voice &amp; Tone</h2>
    <div class="photo" role="img" aria-label="Smiling patient during a dental check-up"></div>
    <div class="tbox" style="top:25.7px"><h3>Personality</h3><p>“The Trusted Expert”</p></div>
    <div class="tbox" style="top:62.6px"><h3>Authoritative without intimidating</h3><p>Clinical expertise communicated warmly</p></div>
    <div class="tbox" style="top:98.9px"><h3>Calculated precision</h3><p>Every word chosen deliberately for impact</p></div>
    <div class="tbox" style="top:135.2px"><h3>Professional yet personal</h3><p>Technical knowledge made accessible</p></div>
    <div class="tbox" style="top:172.7px"><h3>Empowering not patronising</h3><p>Educates patients to make informed decisions</p></div>
  </section>

  <!-- Universal messages -->
  <section class="slide messages">
    <div class="abs wordmark">The Mark Lantern</div>
    <h2 class="abs heading">Universal Brand Messages</h2>
    <div class="abs band">
      <div class="msg">
        <svg viewBox="0 0 26 28" fill="none" stroke="#fff" stroke-width="1.3"><path d="M13 2 23 6v8c0 6-4 10-10 12C7 24 3 20 3 14V6z"/><path d="M13 5l7 3v6c0 4-3 7-7 9-4-2-7-5-7-9V8z"/><path d="M9 14l3 3 5-6"/></svg>
        <p>20+ years of<br>fellowship-trained<br>expertise you can trust</p>
      </div>
      <div class="msg">
        <svg viewBox="0 0 26 28" fill="none" stroke="#fff" stroke-width="1.3"><circle cx="13" cy="9" r="5"/><path d="M13 6.5v5M10.5 9h5"/><path d="M2 12v7l6 6h4v-5l-4-4M24 12v7l-6 6h-4v-5l4-4"/></svg>
        <p>Complex cases solved<br>with precision and<br>genuine care</p>
      </div>
      <div class="msg">
        <svg viewBox="0 0 26 28" fill="none" stroke="#fff" stroke-width="1.3"><circle cx="13" cy="14" r="11"/><circle cx="13" cy="14" r="5"/><path d="M13 3v6M13 19v6M2 14h6M18 14h6"/></svg>
        <p>Holistic treatment for<br>function, health, and<br>confidence</p>
      </div>
      <div class="msg">
        <svg viewBox="0 0 26 28" fill="none" stroke="#fff" stroke-width="1.3"><path d="M3 26V6h20v20z"/><path d="M8 6V2h10v4M3 11h20"/><path d="M7 26v-9h4v9M15 26v-9h4v9"/></svg>
        <p>Three convenient<br>locations, one<br>exceptional standard</p>
      </div>
    </div>
  </section>

  <!-- Section divider -->
  <section class="slide divider">
    <div class="abs wordmark">The Mark Lantern</div>
    <div class="abs num">01</div>
    <h2 class="abs heading">WL Ortho<br>(Westlake)</h2>
  </section>

  <!-- Clinic overview -->
  <section class="slide overview">
    <div class="abs head"><div class="abs wordmark light">The Mark Lantern</div><h2>Clinic Overview</h2></div>

    <div class="card" style="left:12.3px;top:46.4px">
      <svg viewBox="0 0 16 16" fill="none" stroke="#553a8c" stroke-width="1"><path d="M8 15s5-5 5-9A5 5 0 0 0 3 6c0 4 5 9 5 9z"/><circle cx="8" cy="6" r="1.8"/></svg>
      <h3>Location</h3><p>48 Linden Lane, Westlake - boutique practice in Melbourne’s heart</p>
    </div>
    <div class="card" style="left:144.2px;top:46.4px">
      <svg viewBox="0 0 16 16" fill="none" stroke="#553a8c" stroke-width="1"><circle cx="7" cy="9" r="6"/><circle cx="7" cy="9" r="3"/><path d="M7 9l7-7M12 1v3h3"/></svg>
      <h3>Positioning</h3><p>Luxury, high-aesthetic<br>orthodontic destination</p>
    </div>
    <div class="card" style="left:275.5px;top:46.4px">
      <svg viewBox="0 0 16 16" fill="none" stroke="#553a8c" stroke-width="1"><circle cx="8" cy="4" r="2.5"/><path d="M1 11h4v4H1zM6 11h4v4H6zM11 11h4v4h-4zM8 7v4"/></svg>
      <h3>Key Differentiator</h3><p>Diamond ClearPath Provider with boutique luxury experience</p>
    </div>
    <div class="card" style="left:12.3px;top:101.1px">
      <svg viewBox="0 0 16 16" fill="none" stroke="#553a8c" stroke-width="1"><path d="M3 1v14M8 1v14M13 1v14"/><circle cx="3" cy="5" r="1.2"/><circle cx="8" cy="9" r="1.2"/><circle cx="13" cy="6" r="1.2"/></svg>
      <h3>Primary Services</h3><p>ClearPath (specialising in complex cases),traditional braces, lingual braces, early orthodontic intervention</p>
    </div>
    <div class="card" style="left:144.2px;top:101.1px">
      <svg viewBox="0 0 16 16" fill="none" stroke="#553a8c" stroke-width="1"><path d="M2 15V6h12v9zM5 6V2h6v4M1 15h14"/><path d="M5 15v-5h2v5M9 15v-5h2v5"/></svg>
      <h3>Clinic Environment</h3><p>Boutique-style practice with luxury aesthetic, cutting-edge equipment</p>
    </div>
    <div class="card" style="left:275.5px;top:101.1px">
      <svg viewBox="0 0 16 16" fill="none" stroke="#553a8c" stroke-width="1"><circle cx="8" cy="8" r="6.5"/><path d="M8 4v4l3 2"/></svg>
      <h3>Operating Hours</h3><p>Monday-Thursday: 8am-5pm, Friday: Closed, Weekend: Closed</p>
    </div>
    <div class="card" style="left:12.3px;top:157.6px">
      <svg viewBox="0 0 16 16" fill="none" stroke="#553a8c" stroke-width="1"><path d="M1 3h3M1 8h3M1 13h3M6 3h9M6 8h9M6 13h9"/></svg>
      <h3>Unique Features</h3><p>All-inclusive treatment quotes, flexible payment plans up to 24 months</p>
    </div>
    <div class="photo" role="img" aria-label="Smiling patient receiving orthodontic care"></div>
  </section>

  <!-- Closing -->
  <section class="slide closing">
    <div class="abs wordmark light">The Mark Lantern</div>
    <div class="abs rule" style="top:108px"></div>
    <div class="abs thanks">Thank You</div>
    <div class="abs rule" style="top:169px"></div>
  </section>

</main>
</body>
</html>
```